Dental care for hole family, announcement in newspaper

Hey! I have Dental surgery Business in middle of Finland in Jyväskylä. You can see my web www.hammasvelmora.fi.
Now I am looking for new way to do advertisement, more visual I hope.
I woul like to have announcement in newspaper. I would like to tell that we treating hole family from babyes to seniors. I saw here in your pages cute photo where about 1-year old baby was brushing teeth ja looking with big eys to me. It is the feeling I am looking for. My idea is to tell people, that in our klinik, they can have "own dental hygienist" who is taking care of them with dentists of different spesialitis.
Now I need advertisements for that information!!

Yours, Velmora

Target Market(s)

All.

Industry/Entity Type

Dental Clinic

Requirements
Must have
• Visual components, whicts are matching with my homepages visual look (www.hammasvelmora.fi).
Nice to have
• My logo, whitch you can find from my webpages.

```html
<!DOCTYPE html>
<html lang="en">
<head>
<meta charset="utf-8">
<title>Hammasvelmora – newspaper announcement</title>
<link rel="stylesheet" href="https://fonts.googleapis.com/css2?family=Mulish:wght@400;500;600&display=swap">
<style>
  :root {
    --brown: #6b4e2c;
    --sky: #55c3ec;
    --amber: #f9b215;
    --white: #ffffff;
    --photo-skin: #f0c4ad;
    --photo-skin-light: #f7dccf;
    --photo-light: #eeedea;
    --logo-text: #5a3d1f;
  }
  * { box-sizing: border-box; margin: 0; padding: 0; }
  html, body { width: 1200px; height: 879px; overflow: hidden; background: var(--white); }
  body { font-family: "Mulish", sans-serif; }
  .ad { position: relative; width: 1200px; height: 879px; background: var(--white); }

  .ad__photo {
    position: absolute; left: 0; top: 0; width: 1200px; height: 555px;
    background:
      radial-gradient(ellipse 560px 470px at 300px 300px, var(--photo-skin) 0%, var(--photo-skin) 45%, var(--photo-skin-light) 70%, rgba(247,220,207,0) 100%),
      linear-gradient(90deg, #f5f3f1 0%, #fbfbfa 55%, var(--photo-light) 70%, var(--photo-light) 100%);
  }

  .ad__message {
    position: absolute; left: 727px; top: 204px; width: 473px; height: 351px;
    background: var(--brown);
    padding: 76px 0 0 49px;
    color: var(--white);
    font-size: 41px; font-weight: 500; line-height: 48px;
  }
  .ad__message-accent { color: var(--amber); font-weight: 600; }

  .ad__contact {
    position: absolute; left: 0; top: 555px; width: 1200px; height: 62px;
    background: var(--sky);
    display: flex; align-items: center; justify-content: center; gap: 26px;
    color: var(--white); font-size: 31px; font-weight: 500;
    padding-left: 60px;
  }
  .ad__contact-item { display: flex; align-items: center; gap: 6px; }
  .ad__contact-item svg { flex: none; }
  .ad__rule { position: absolute; left: 0; top: 617px; width: 1200px; height: 8px; background: var(--amber); }

  .ad__brand {
    position: absolute; right: 311px; top: 690px;
    text-align: right; color: var(--logo-text); font-weight: 400;
  }
  .ad__brand-sub { font-size: 31px; line-height: 36px; letter-spacing: 0.5px; }
  .ad__brand-name { font-size: 58px; line-height: 64px; letter-spacing: 3px; text-transform: uppercase; }
  .ad__brand-partner { display: flex; justify-content: flex-end; align-items: center; margin-top: 0; }
  .ad__brand-dot { width: 20px; height: 20px; border-radius: 50%; background: var(--amber); margin-right: 112px; }
</style>
</head>
<body>
  <main class="ad">
    <div class="ad__photo" role="img" aria-label="Photo of a baby brushing its teeth with a white and blue toothbrush, looking at the viewer with big eyes, on a light grey background"></div>

    <div class="ad__message">
      <p><span class="ad__message-accent">BESPOKE</span>, gentle<br>dental care and<br>personal hygienist<br>for all ages</p>
    </div>

    <div class="ad__contact">
      <span class="ad__contact-item">
        <svg width="24" height="24" viewBox="0 0 24 24" aria-hidden="true">
          <circle cx="12" cy="12" r="10" fill="none" stroke="#fff" stroke-width="2"/>
          <path d="M9 7c-1 1-1 3 1 6s4 4 5 4l1-2-2-1-1 1c-1-.5-2-2-2.5-3l1-1-1-2z" fill="#fff"/>
        </svg>
        014 555 019
      </span>
      <span class="ad__contact-item">
        <svg width="30" height="22" viewBox="0 0 30 22" aria-hidden="true">
          <rect x="1.5" y="1.5" width="27" height="19" fill="none" stroke="#fff" stroke-width="2"/>
          <path d="M2 2l13 10L28 2" fill="none" stroke="#fff" stroke-width="2"/>
        </svg>
        hammasvelmora@aurterveys.fi
      </span>
    </div>
    <div class="ad__rule"></div>

    <div class="ad__brand">
      <p class="ad__brand-sub">Hammaslääkäriasema</p>
      <p class="ad__brand-name">Hammasvelmora</p>
      <div class="ad__brand-partner"><span class="ad__brand-dot"></span></div>
    </div>
  </main>
</body>
</html>
```